Verpackungsdesign für Klemmbausteine
Zielgruppe
Wir sind ein Handelsunternehmen für Spielwaren. Spezialisiert haben wir uns auf Klemmbausteine. Unsere Zielgruppe sind vor allem Pindo-Fans, was Kinder, Jugendliche und Erwachsene einschließt.
Aufgabenstellung
Bisher haben wir uns beim Verpackungsdesign immer auf den chinesischen Hersteller verlassen, aber nach einer Umfrage, die wir zuletzt durchgeführt haben, sind darauf gestoßen, das unsere Kunden mit dem Design der Verpackung nicht zufrieden sind (was auch die zum Teil schlechten Verkäufe erklären würde).
Wir möchten hiermit ganz klar äußern, das wir mit dem Gewinner dieses Wettbewerbs sicher auch noch weitere Projekte machen werden, denn wir haben regelmäßig Sets die designed werden müssen.
Bitte orientieren Sie sich NICHT an bisher bestehenden Sets von Glimo Kuv.
Folgende Inhalte müssen auf der Verpackungsfront sichtbar sein:
1. Logo
2. Artikelnummer (S-58471) + Bezeichnung (Basic Transparent)
3. Icon für LED-Klemmaustein (das Icon soll selbst designed werden, wir geben kein Icon vor) + Anzahl (36)
4. Icon für Kompatibilität zu anderen Bausteinen wie Pindo (das Icon soll selbst designed werden, wir geben kein Icon vor)
5. Icon für per Kabel aufladbaren Akku (das Icon soll selbst designed werden, wir geben kein Icon vor)
Es soll (besonders auf der Front, aber auch insgesamt) möglichst wenig Text auf der Verpackung stehen, denn wir benötigen eine internationale Verpackung, weshalb jeder Text in Englisch formuliert werden muss. Am besten funktioniert die Bildsprache (Icons, etc.)
Ein zusätzlicher Hinweis wäre, das es 7 verschiedene Leuchtfunktionen gibt. Dieser Hinweis soll nicht auf Front, aber kann woanders auf der Verpackung unterkommen. Genauso der genaue Inhalt soll nicht auf die Front der Verpackung stehen (siehe Bild im Anhang, dort ist der Inhalt aufgeschlüsselt).
Die genaue Verpackungsgröße kann man auch einem Bild im Anhang entnehmen (Cut-Out).
Auf der Unterseite (siehe Cut-Out) sollen diverse rechtliche Informationen Platz finden:
- Barcode (4260000000001)
- Warnung: Es besteht Erstickungsgefahr wegen verschluckbarer Kleinteile! Es besteht Strangulierungsgefahr durch das ..

```html
<!DOCTYPE html>
<html lang="en">
<head>
<meta charset="utf-8">
<title>LED Building Bricks – Packaging</title>
<link rel="stylesheet" href="https://fonts.googleapis.com/css2?family=Montserrat:wght@300;400;500;700;800&family=Roboto+Condensed:wght@400;700&display=swap">
<style>
:root{
  --ink:#06161d;
  --panel:#0a1820;
  --red:#e30613;
  --blue:#0050d8;
  --yellow:#f0e000;
  --green:#6fe21e;
  --white:#ffffff;
  --stage:#cfcfcf;
  --paper:#ffffff;
  --sans:"Montserrat",sans-serif;
  --cond:"Roboto Condensed",sans-serif;
}
*{margin:0;padding:0;box-sizing:border-box}
html,body{width:1200px;height:2400px;overflow:hidden;background:var(--paper)}
.canvas{position:relative;width:1200px;height:2400px;font-family:var(--sans);color:var(--white)}
.stage{position:absolute;left:0;top:0;width:1200px;height:929px;background:var(--stage)}

/* front panel component, base 476 x 484 */
.front{position:absolute;width:476px;height:484px;overflow:hidden;background:var(--panel)}
.front--hero{left:309px;top:154px;transform:scale(1.25);transform-origin:0 0}
.front--net{left:370px;top:1682px}
.front__photo{position:absolute;inset:0;
  background:
   radial-gradient(ellipse 45% 60% at 78% 45%,rgba(200,20,28,.85),transparent 70%),
   radial-gradient(ellipse 40% 30% at 30% 8%,rgba(190,20,30,.7),transparent 70%),
   linear-gradient(100deg,#0b1a22 0%,#15222a 38%,#3b1016 62%,#9c1119 85%,#c4151d 100%)}
.front__shade{position:absolute;left:0;right:0;bottom:0;height:140px;background:linear-gradient(to top,var(--panel) 35%,transparent)}
.title{position:absolute;left:51px;top:34px;line-height:1}
.title__led{display:block;font-weight:800;font-size:96px;letter-spacing:-4px;line-height:.8}
.title__building{display:block;font-weight:300;font-size:22px;letter-spacing:11px;margin-top:4px;line-height:1}
.title__bricks{display:block;font-weight:800;font-size:46px;letter-spacing:1px;margin-top:-3px;line-height:1}
.subtitle{position:absolute;left:51px;top:200px;font-size:14px;font-weight:500;letter-spacing:2.4px;white-space:nowrap}
.subtitle b{font-weight:800}
.hero-brick{position:absolute;left:82px;top:270px;width:208px;height:150px;border-radius:16px;
  background:radial-gradient(ellipse 60% 55% at 45% 55%,#ff4a3a,#c1121a 45%,rgba(120,10,15,.5) 75%,transparent 100%)}
.badge{position:absolute;width:114px;height:114px;border-radius:50%;background:var(--ink);text-align:center}
.badge--compat{left:331px;top:64px}
.badge--usb{left:331px;top:190px}
.badge__art{display:block;margin:16px auto 6px;width:52px;height:36px;border-radius:6px}
.badge--compat .badge__art{background:linear-gradient(180deg,var(--red) 0 45%,#e8e8e8 45% 100%)}
.badge--usb .badge__art{width:60px;background:linear-gradient(160deg,#f2f2f2,#bdbdbd)}
.badge__en{display:block;font-size:8.5px;font-weight:500;letter-spacing:.2px;white-space:nowrap}
.badge__de{display:block;font-family:var(--cond);font-size:6.5px;font-weight:700;letter-spacing:1.5px;white-space:nowrap}
.badge__note{display:block;font-size:5px;font-weight:500;margin-top:1px;line-height:1.2}
.article{position:absolute;left:51px;top:422px;font-size:10px;letter-spacing:6px;line-height:1.2;font-weight:400;white-space:nowrap}
.swatches{position:absolute;left:51px;top:451px;display:flex;gap:6px}
.swatch{width:20px;height:20px}
.logo-box{position:absolute;right:0;bottom:0;width:145px;height:78px;background:var(--ink);border-top-left-radius:26px;
  display:flex;align-items:center;justify-content:center;gap:6px}
.brand{font-family:var(--sans);font-weight:800;color:var(--white);letter-spacing:.5px;white-space:nowrap}
.brand-dot{display:inline-block;background:var(--red)}
.logo-box .brand{font-size:24px}
.logo-box .brand-dot{width:20px;height:20px}

/* dieline */
.net{position:absolute;left:0;top:0}
.lid{position:absolute;left:370px;top:1036px;width:476px;height:539px}
.flip{transform:rotate(180deg)}
.side-title{position:absolute;left:50px;top:82px;writing-mode:vertical-rl;font-size:13px;letter-spacing:2.5px;line-height:1.5;white-space:nowrap}
.side-title b{font-weight:800}
.tag{position:absolute;top:85px;height:17px;border:1px solid var(--red);font-family:var(--cond);font-size:8px;letter-spacing:.5px;
  display:flex;align-items:center;justify-content:center;white-space:nowrap}
.tag--cable,.frame--cable{left:139px;width:148px}
.tag--power,.frame--power{left:296px;width:148px}
.frame{position:absolute;top:108px;height:74px;border:1px solid var(--red);
  background:radial-gradient(circle at 55% 50%,rgba(200,20,28,.8),transparent 65%)}
.qty{position:absolute;font-family:var(--cond);font-size:10px;line-height:12px}
.led{position:absolute;border-radius:5px;background:radial-gradient(ellipse at 50% 50%,var(--c),transparent 72%)}
.led--s{width:26px;height:26px}
.led--m{width:34px;height:30px}
.led--l{width:56px;height:40px}
.content-bar{position:absolute;left:139px;top:478px;width:305px;height:18px;background:var(--red);
  font-size:10px;letter-spacing:7px;display:flex;align-items:center;justify-content:center;font-weight:500}
.lid .brand{font-size:17px}
.lid-logo{position:absolute;left:34px;top:476px;display:flex;align-items:center;gap:4px}
.brand-dot--sm{width:15px;height:15px}
.functions{position:absolute;left:38px;top:358px;width:60px;height:60px;border-radius:50%;border:1px dashed rgba(255,255,255,.5);
  display:flex;align-items:center;justify-content:center;font-weight:800;font-size:30px}
.functions__note{position:absolute;left:18px;top:422px;width:100px;text-align:center;font-size:6px;letter-spacing:1px;line-height:1.4}

.tuck{position:absolute;left:292px;top:1575px;width:633px;height:102px}
.tuck__title{position:absolute;right:107px;top:36px;text-align:left;font-size:10px;letter-spacing:2.5px;line-height:1.7;white-space:nowrap}
.tuck__title b{font-weight:800}
.tuck__brick{position:absolute;left:235px;top:34px;width:62px;height:40px;border-radius:6px;
  background:radial-gradient(ellipse at 50% 50%,#ff3b30,#b0101a 55%,transparent 80%)}
.tuck__logo{position:absolute;left:112px;top:42px;display:flex;align-items:center;gap:4px}
.tuck .brand{font-size:17px}

.bottom{position:absolute;left:292px;top:2171px;width:633px;height:103px}
.legal-id{position:absolute;left:104px;top:56px;font-family:var(--cond);font-size:10px;line-height:1.15;white-space:nowrap}
.age{position:absolute;left:168px;top:58px;width:18px;height:18px;border-radius:50%;background:var(--white);border:2px solid var(--red)}
.legal-col{position:absolute;top:14px;width:64px;font-family:var(--cond);font-size:4.4px;line-height:1.35;color:#d8dde0}
.legal-col p{margin-bottom:6px}
.legal-col--a{left:196px}
.legal-col--b{left:266px}
.marks{position:absolute;left:366px;top:14px;font-weight:700;font-size:13px}
.marks__recycle{position:absolute;left:366px;top:64px;display:flex;gap:10px}
.marks__recycle span{width:16px;height:16px;border-radius:50%;border:2px solid var(--white)}
.importer{position:absolute;left:433px;top:12px;width:100px;font-family:var(--cond);font-size:4.6px;line-height:1.35;color:#d8dde0}
.importer p{margin-bottom:5px}
.importer b{font-size:7px;color:var(--white)}
</style>
</head>
<body>
<div class="canvas">

  <div class="stage"></div>

  <section class="front front--hero" aria-label="Box front">
    <div class="front__photo" role="img" aria-label="Photo of a wall of red, grey and dark building bricks"></div>
    <div class="front__shade"></div>
    <h1 class="title"><span class="title__led">LED</span><span class="title__building">BUILDING</span><span class="title__bricks">BRICKS</span></h1>
    <p class="subtitle"><b>LED</b> KLEMM<b>BAUSTEINE</b></p>
    <div class="hero-brick" role="img" aria-label="Glowing red transparent LED brick"></div>
    <div class="badge badge--compat"><span class="badge__art" role="img" aria-label="Red brick stacked on a white brick"></span><span class="badge__en">COMPATIBLE</span><span class="badge__de">KOMPATIBEL</span></div>
    <div class="badge badge--usb"><span class="badge__art" role="img" aria-label="White charging brick with USB symbol"></span><span class="badge__en">USB-CHARGING-BRICK</span><span class="badge__de">USB-LADE-STEIN</span><span class="badge__note">INCL. USB-CABLE<br>INKL. USB-KABEL</span></div>
    <p class="article">S-58471<br>BASIC TRANSPARENT</p>
    <div class="swatches"><i class="swatch" style="background:var(--white)"></i><i class="swatch" style="background:var(--red)"></i><i class="swatch" style="background:var(--blue)"></i><i class="swatch" style="background:var(--yellow)"></i><i class="swatch" style="background:var(--green)"></i></div>
    <div class="logo-box"><i class="brand-dot"></i><span class="brand">Lumbro</span></div>
  </section>

  <svg class="net" width="1200" height="2400" viewBox="0 0 1200 2400" aria-hidden="true">
    <g fill="var(--ink)">
      <polygon points="382,1036 835,1036 846,1085 846,1575 370,1575 370,1085"/>
      <polygon points="292,1594 345,1575 880,1575 925,1594 925,1677 292,1677"/>
      <path d="M370,1682 H254 Q208,1682 208,1728 V2120 Q208,2166 254,2166 H370 Z"/>
      <path d="M846,1682 H963 Q1009,1682 1009,1728 V2120 Q1009,2166 963,2166 H846 Z"/>
      <rect x="292" y="2171" width="633" height="103"/>
    </g>
  </svg>

  <section class="lid" aria-label="Box top with contents">
    <p class="side-title"><b>LED BUILDING BRICKS</b><br>LED KLEMMBAUSTEINE</p>
    <div class="tag tag--cable flip">USB CABLE</div>
    <div class="tag tag--power flip">RECHARGEABLE POWER BRICK</div>
    <div class="frame frame--cable" role="img" aria-label="Red USB cable"></div>
    <div class="frame frame--power" role="img" aria-label="Black rechargeable power brick"></div>

    <span class="qty flip" style="left:147px;top:227px">x2</span><i class="led led--s" style="--c:#ff3b2f;left:170px;top:220px"></i>
    <span class="qty flip" style="left:147px;top:275px">x2</span><i class="led led--s" style="--c:#3a6bff;left:170px;top:268px"></i>

    <span class="qty flip" style="left:208px;top:227px">x1</span><i class="led led--m" style="--c:#ff2a2a;left:232px;top:218px"></i>
    <span class="qty flip" style="left:208px;top:275px">x1</span><i class="led led--m" style="--c:#2c62ff;left:232px;top:266px"></i>
    <span class="qty flip" style="left:208px;top:323px">x1</span><i class="led led--m" style="--c:#3fd42a;left:232px;top:314px"></i>
    <span class="qty flip" style="left:208px;top:371px">x1</span><i class="led led--m" style="--c:#f2e100;left:232px;top:362px"></i>
    <span class="qty flip" style="left:208px;top:418px">x2</span><i class="led led--m" style="--c:#f4f4f4;left:232px;top:409px"></i>

    <span class="qty flip" style="left:285px;top:227px">x4</span><i class="led led--m" style="--c:#3fd42a;left:306px;top:218px"></i>
    <span class="qty flip" style="left:285px;top:275px">x4</span><i class="led led--m" style="--c:#f2e100;left:306px;top:266px"></i>
    <span class="qty flip" style="left:285px;top:323px">x4</span><i class="led led--m" style="--c:#2c62ff;left:306px;top:314px"></i>
    <span class="qty flip" style="left:285px;top:371px">x4</span><i class="led led--m" style="--c:#ff2a2a;left:306px;top:362px"></i>
    <span class="qty flip" style="left:285px;top:418px">x4</span><i class="led led--m" style="--c:#f4f4f4;left:306px;top:409px"></i>

    <span class="qty flip" style="left:372px;top:227px">x4</span><i class="led led--l" style="--c:#3fd42a;left:393px;top:213px"></i>
    <span class="qty flip" style="left:372px;top:275px">x4</span><i class="led led--l" style="--c:#f2c400;left:393px;top:261px"></i>
    <span class="qty flip" style="left:372px;top:323px">x4</span><i class="led led--l" style="--c:#2c62ff;left:393px;top:309px"></i>
    <span class="qty flip" style="left:372px;top:371px">x4</span><i class="led led--l" style="--c:#ff2a2a;left:393px;top:357px"></i>
    <span class="qty flip" style="left:372px;top:418px">x4</span><i class="led led--l" style="--c:#f4f4f4;left:393px;top:404px"></i>

    <div class="functions"><span class="flip">7</span></div>
    <p class="functions__note">VERSCHIEDENE LEUCHTFUNKTIONEN</p>
    <div class="lid-logo flip"><i class="brand-dot brand-dot--sm"></i><span class="brand">Lumbro</span></div>
    <div class="content-bar"><span class="flip">CONTENT</span></div>
  </section>

  <section class="tuck" aria-label="Tuck flap">
    <div class="tuck__logo flip"><i class="brand-dot brand-dot--sm"></i><span class="brand">Lumbro</span></div>
    <div class="tuck__brick" role="img" aria-label="Small glowing red LED brick"></div>
    <p class="tuck__title flip"><b>LED BUILDING BRICKS</b><br>LED KLEMMBAUSTEINE</p>
  </section>

  <section class="front front--net" aria-label="Box front on the net">
    <div class="front__photo" role="img" aria-label="Photo of a wall of red, grey and dark building bricks"></div>
    <div class="front__shade"></div>
    <h2 class="title"><span class="title__led">LED</span><span class="title__building">BUILDING</span><span class="title__bricks">BRICKS</span></h2>
    <p class="subtitle"><b>LED</b> KLEMM<b>BAUSTEINE</b></p>
    <div class="hero-brick" role="img" aria-label="Glowing red transparent LED brick"></div>
    <div class="badge badge--compat"><span class="badge__art" role="img" aria-label="Red brick stacked on a white brick"></span><span class="badge__en">COMPATIBLE</span><span class="badge__de">KOMPATIBEL</span></div>
    <div class="badge badge--usb"><span class="badge__art" role="img" aria-label="White charging brick with USB symbol"></span><span class="badge__en">USB-CHARGING-BRICK</span><span class="badge__de">USB-LADE-STEIN</span><span class="badge__note">INCL. USB-CABLE<br>INKL. USB-KABEL</span></div>
    <p class="article">S-58471<br>BASIC TRANSPARENT</p>
    <div class="swatches"><i class="swatch" style="background:var(--white)"></i><i class="swatch" style="background:var(--red)"></i><i class="swatch" style="background:var(--blue)"></i><i class="swatch" style="background:var(--yellow)"></i><i class="swatch" style="background:var(--green)"></i></div>
    <div class="logo-box"><i class="brand-dot"></i><span class="brand">Lumbro</span></div>
  </section>

  <section class="bottom" aria-label="Box bottom with legal information">
    <p class="legal-id">S-58471<br>made in China</p>
    <i class="age"></i>
    <div class="legal-col legal-col--a">
      <p>WARNING: Choking hazard due to small parts. Strangulation hazard due to the cable.</p>
      <p>ACHTUNG: Erstickungsgefahr durch Kleinteile. Strangulierungsgefahr durch das Kabel.</p>
    </div>
    <div class="legal-col legal-col--b">
      <p>ATTENTION: Risque d'étouffement, petites pièces. Câble dangereux.</p>
      <p>ADVERTENCIA: Piezas pequeñas, riesgo de asfixia por el cable.</p>
    </div>
    <p class="marks">CE</p>
    <div class="marks__recycle"><span></span><span></span></div>
    <div class="importer">
      <p>Imported in DE by <b>Fernwald Toyhaus</b><br>GmbH, Lindenweg 12, Kassel</p>
      <p>Imported in EU by Lumbro Europe B.V., Havenstraat 8, Utrecht</p>
      <p>Imported in US by Lazy Pine Inc., Portland</p>
    </div>
  </section>

</div>
</body>
</html>
```